KORBALT

The business want a professional looking business card. We have a scetch we will add but want the extra upgrade, and would like more suggestions for variations of our business cards.

```html
<!DOCTYPE html>
<html lang="en">
<head>
<meta charset="utf-8">
<title>KORBALT Business Card</title>
<link rel="stylesheet" href="https://fonts.googleapis.com/css2?family=Marcellus&family=Questrial&display=swap">
<style>
  :root {
    --canvas: #dedede;
    --cream: #f4eed8;
    --brown: #3e2a15;
    --gold: #b0935a;
    --gold-light: #d2b77c;
    --ink: #3a3026;
    --serif: "Marcellus", Georgia, serif;
    --sans: "Questrial", Arial, sans-serif;
  }
  * { box-sizing: border-box; margin: 0; padding: 0; }
  html, body { width: 906px; height: 1200px; overflow: hidden; }
  body { background: var(--canvas); position: relative; }

  .card {
    position: absolute;
    left: 53px;
    width: 800px;
    height: 470px;
  }
  .card--front { top: 130px; background: var(--cream); }
  .card--back  { top: 660px; background: var(--brown); }

  /* Front */
  .front__company {
    position: absolute; left: 77px; top: 50px;
    font-family: var(--serif); font-size: 38px; color: var(--gold);
    letter-spacing: 0.5px; white-space: nowrap;
  }
  .front__rule {
    position: absolute; left: 77px; top: 110px;
    width: 490px; height: 1.5px; background: var(--gold);
  }
  .front__name {
    position: absolute; left: 77px; top: 150px;
    font-family: var(--serif); font-size: 31px; color: var(--ink);
    letter-spacing: 0.5px; white-space: nowrap;
  }
  .front__role {
    position: absolute; left: 77px; top: 194px;
    font-family: var(--sans); font-size: 25px; color: var(--ink);
  }
  .contact-list { position: absolute; left: 77px; top: 268px; list-style: none; }
  .contact-list__item {
    display: flex; align-items: center; height: 40px; margin-bottom: 17px;
    font-family: var(--sans); font-size: 26px; color: var(--ink);
  }
  .contact-list__icon {
    width: 40px; height: 40px; border-radius: 4px; background: var(--gold);
    margin-right: 20px; flex: none;
  }
  .front__brand {
    position: absolute; left: 555px; top: 215px; width: 200px;
    text-align: center;
  }
  .brand-dot {
    display: block; margin: 0 auto 18px;
    width: 64px; height: 64px; border-radius: 50%; background: var(--gold);
  }
  .brand-name {
    font-family: var(--serif); font-size: 30px; color: var(--gold);
    letter-spacing: 4px;
  }

  /* Back */
  .back__brand { position: absolute; left: 0; top: 55px; width: 100%; text-align: center; }
  .back__dot {
    display: block; margin: 0 auto;
    width: 150px; height: 150px; border-radius: 50%; background: var(--gold-light);
  }
  .back__name {
    margin-top: 52px;
    font-family: var(--serif); font-size: 68px; color: var(--gold-light);
    letter-spacing: 18px; padding-left: 18px; line-height: 1;
  }
  .back__since {
    margin-top: 32px;
    font-family: var(--sans); font-size: 24px; color: var(--gold-light);
    letter-spacing: 5px; padding-left: 5px;
  }
</style>
</head>
<body>
  <section class="card card--front" aria-label="Business card front">
    <div class="front__company">KORBALT F HOLMVIK</div>
    <div class="front__rule"></div>
    <div class="front__name">LARS ANDERS HOLMVIK</div>
    <div class="front__role">CEO &amp; Founder</div>
    <ul class="contact-list">
      <li class="contact-list__item">
        <svg class="contact-list__icon" viewBox="0 0 40 40" aria-hidden="true">
          <rect width="40" height="40" rx="4" fill="#b0935a"/>
          <path d="M13 10c2 0 3 4 3 5s-2 2-2 3c1 3 4 6 7 7 1 0 2-2 3-2s5 1 5 3-2 4-4 4C16 30 10 24 10 15c0-2 1-5 3-5z" fill="#f4eed8"/>
        </svg>
        004795550142
      </li>
      <li class="contact-list__item">
        <svg class="contact-list__icon" viewBox="0 0 40 40" aria-hidden="true">
          <rect width="40" height="40" rx="4" fill="#b0935a"/>
          <rect x="9" y="12" width="22" height="16" fill="none" stroke="#f4eed8" stroke-width="2"/>
          <path d="M9 12l11 9 11-9" fill="none" stroke="#f4eed8" stroke-width="2"/>
        </svg>
        korbalt.llc@mailbox.com
      </li>
      <li class="contact-list__item">
        <svg class="contact-list__icon" viewBox="0 0 40 40" aria-hidden="true">
          <rect width="40" height="40" rx="4" fill="#b0935a"/>
          <g fill="none" stroke="#f4eed8" stroke-width="1.6">
            <circle cx="20" cy="20" r="10"/>
            <ellipse cx="20" cy="20" rx="4.5" ry="10"/>
            <path d="M10 20h20M12 15h16M12 25h16"/>
          </g>
        </svg>
        www.korbalt.llc
      </li>
    </ul>
    <div class="front__brand">
      <span class="brand-dot"></span>
      <div class="brand-name">KORBALT</div>
    </div>
  </section>

  <section class="card card--back" aria-label="Business card back">
    <div class="back__brand">
      <span class="back__dot"></span>
      <div class="back__name">KORBALT</div>
      <div class="back__since">SINCE 2026</div>
    </div>
  </section>
</body>
</html>
```